Mr Pellows Lawn Care flyer for newsletter

I need a professional looking flyer design for my company Mr Pellows Lawn Care based in New Braunfels, TX to boost sales. Must include the following: Lawn service starting at $40 (mowing, edging, leaf blowing) Tree trimming starting at $125. Other services-mulching, shrub trimming, aeration, flower bed maintenance, Fall/spring clean up. Serving New Braunfels and surrounding areas. To set up and estimate please call 830 247 3091 or email mrpellowslawn@brimfield-mail.com

Industry/Entity Type

Landscaping

Font styles to use
Serif

Colors

Designer to choose colors to be used in the design.

Requirements
Must have
• Phone number 830 247 3091
• Email mrpellowslawn@brimfield-mail.com

```html
<!DOCTYPE html>
<html lang="en">
<head>
<meta charset="utf-8">
<title>Mr Pellows Lawn Care – Flyer</title>
<link rel="stylesheet" href="https://fonts.googleapis.com/css2?family=Cinzel:wght@700;900&family=Open+Sans:wght@400;600;700;800&display=swap">
<style>
  :root {
    --forest: #1d4a2a;
    --leaf: #3f9a3a;
    --grass-light: #8cc63f;
    --grass: #4e9a2c;
    --lawn-deep: #3d7a2a;
    --mulch: #d3c2a6;
    --mulch-light: #ddd0b8;
    --crimson: #a51c22;
    --crimson-text: #b3262b;
    --white: #ffffff;
  }
  * { box-sizing: border-box; margin: 0; padding: 0; }
  html, body { width: 927px; height: 1200px; overflow: hidden; background: var(--white); }
  .flyer {
    position: relative; width: 927px; height: 1200px; overflow: hidden;
    font-family: "Open Sans", Arial, sans-serif; background: var(--white);
  }

  /* Header */
  .header-texture {
    position: absolute; left: 0; top: 0; width: 927px; height: 273px;
    background: linear-gradient(180deg, var(--mulch) 0%, var(--mulch-light) 70%, var(--grass-light) 100%);
  }
  .brand {
    position: absolute; left: 0; top: 34px; width: 927px; text-align: center;
    color: var(--forest); font-weight: 800;
  }
  .brand-name { font-size: 100px; line-height: 1; letter-spacing: 1px; }
  .brand-line { font-size: 50px; line-height: 1; letter-spacing: 22px; margin-top: 20px; padding-left: 22px; }
  .header-rule {
    position: absolute; left: 0; top: 273px; width: 927px; height: 6px; background: var(--crimson);
  }

  /* Hero */
  .hero-photo {
    position: absolute; left: 0; top: 279px; width: 927px; height: 380px;
    background: linear-gradient(180deg, var(--lawn-deep) 0%, var(--grass) 100%);
  }
  .hero-title {
    position: absolute; left: 0; top: 588px; width: 927px; text-align: center;
    font-family: "Cinzel", Georgia, serif; font-weight: 900; font-size: 42px;
    color: var(--forest);
    text-shadow: -2px -2px 0 var(--white), 2px -2px 0 var(--white), -2px 2px 0 var(--white), 2px 2px 0 var(--white), 0 3px 4px rgba(0,0,0,.35);
  }

  /* Grass edges */
  .grass-top {
    position: absolute; left: 0; top: 659px; width: 927px; height: 90px;
    background: linear-gradient(180deg, var(--grass) 0%, rgba(140,198,63,.5) 55%, rgba(255,255,255,0) 100%);
  }
  .grass-bottom {
    position: absolute; left: 0; top: 990px; width: 927px; height: 90px;
    background: linear-gradient(0deg, var(--grass) 0%, rgba(140,198,63,.5) 50%, rgba(255,255,255,0) 100%);
  }

  /* Offer boxes */
  .offer {
    position: absolute; left: 30px; width: 515px; height: 162px;
    background: var(--forest); color: var(--white);
  }
  .offer::after {
    content: ""; position: absolute; inset: 6px; border: 1.5px dashed rgba(255,255,255,.85);
  }
  .offer--mowing { top: 686px; }
  .offer--trees { top: 856px; }
  .offer-title { position: absolute; top: 16px; left: 0; width: 100%; text-align: center; font-weight: 700; font-size: 24px; }
  .offer-list { position: absolute; top: 52px; list-style: none; font-size: 23px; line-height: 28.5px; }
  .offer--mowing .offer-list { left: 137px; }
  .offer--trees .offer-list { left: 42px; }
  .price {
    position: absolute; font-weight: 800; font-size: 62px; line-height: 1; color: var(--crimson-text); letter-spacing: -1px;
    text-shadow: -2px -2px 0 var(--white), 2px -2px 0 var(--white), -2px 2px 0 var(--white), 2px 2px 0 var(--white), 0 2px 0 var(--white);
  }
  .price sup { font-size: 32px; vertical-align: 22px; }
  .offer--mowing .price { left: 300px; top: 68px; }
  .offer--trees .price { left: 345px; top: 60px; }

  /* Tick items */
  .tick { position: relative; padding-left: 30px; }
  .tick::before {
    content: ""; position: absolute; left: 0; top: 5px; width: 20px; height: 20px; border-radius: 2px;
    background: var(--white);
  }
  .tick::after {
    content: ""; position: absolute; left: 7px; top: 7px; width: 6px; height: 11px;
    border: solid var(--forest); border-width: 0 3px 3px 0; transform: rotate(45deg);
  }

  /* Other services */
  .other { position: absolute; left: 570px; top: 762px; color: var(--forest); }
  .other-title { font-family: "Cinzel", Georgia, serif; font-weight: 700; font-size: 27px; margin-bottom: 2px; }
  .other-list { list-style: none; font-weight: 700; font-size: 24px; line-height: 29px; }
  .other-list .tick::before { background: var(--forest); }
  .other-list .tick::after { border-color: var(--white); }

  /* Area line */
  .service-area {
    position: absolute; left: 0; top: 1038px; width: 927px; text-align: center;
    font-family: "Cinzel", Georgia, serif; font-weight: 700; font-size: 24px; color: var(--crimson-text);
  }

  /* Footer */
  .footer {
    position: absolute; left: 0; top: 1080px; width: 927px; height: 120px; background: var(--crimson);
    color: var(--white); text-align: center;
  }
  .footer-call { font-weight: 700; font-size: 52px; line-height: 1; margin-top: 16px; display: flex; justify-content: center; align-items: center; gap: 12px; }
  .footer-call svg { width: 44px; height: 44px; }
  .footer-email { font-weight: 700; font-size: 24px; margin-top: 6px; }
</style>
</head>
<body>
<div class="flyer">
  <div class="header-texture" role="img" aria-label="Wood mulch texture with grass fringe"></div>
  <div class="brand">
    <div class="brand-name">MR PELLOWS</div>
    <div class="brand-line">LAWN CARE</div>
  </div>
  <div class="header-rule"></div>

  <div class="hero-photo" role="img" aria-label="Photo of a brick house front with trimmed hedges, flower bed and green lawn"></div>
  <h1 class="hero-title">Professional Lawn Care Services</h1>

  <div class="grass-top" role="img" aria-label="Grass edge"></div>
  <div class="grass-bottom" role="img" aria-label="Grass edge"></div>

  <section class="offer offer--mowing">
    <h2 class="offer-title">Lawn Mowing Services starting at</h2>
    <ul class="offer-list">
      <li class="tick">Mowing</li>
      <li class="tick">Edging</li>
      <li class="tick">Leaf blowing</li>
    </ul>
    <div class="price"><sup>$</sup>40</div>
  </section>

  <section class="offer offer--trees">
    <h2 class="offer-title">Tree Trimming Services starting at</h2>
    <ul class="offer-list">
      <li class="tick">Shrub trimming</li>
      <li class="tick">Aeration</li>
      <li class="tick">Flower bed maintenance</li>
    </ul>
    <div class="price"><sup>$</sup>125</div>
  </section>

  <section class="other">
    <h2 class="other-title">Other services</h2>
    <ul class="other-list">
      <li class="tick">Mulching</li>
      <li class="tick">Shrub trimming</li>
      <li class="tick">Aeration</li>
      <li class="tick">Flower bed maintenance</li>
      <li class="tick">Fall/spring clean up</li>
    </ul>
  </section>

  <p class="service-area">Serving New Braunfels and surrounding area</p>

  <footer class="footer">
    <div class="footer-call">
      <span>Call</span>
      <svg viewBox="0 0 42 42" aria-hidden="true">
        <circle cx="21" cy="21" r="18.5" fill="none" stroke="#fff" stroke-width="2.5"/>
        <path d="M15 11c1.5-1 2.5-.5 3.2.8l1.6 3c.5 1 .2 1.8-.6 2.4l-1.2.9c.8 2.2 2.4 4.3 4.6 5.8l1.1-1c.8-.7 1.6-.8 2.4-.2l2.8 2c1.2.8 1.4 1.9.5 3.2-1.4 2-3.6 2.5-6 1.3-4.6-2.3-8.3-6.6-9.900-11.6-.8-2.5-.2-4.8 1.5-6.6z" fill="#fff"/>
      </svg>
      <span>830 247 3091</span>
    </div>
    <div class="footer-email">or email mrpellowslawn@brimfield-mail.com</div>
  </footer>
</div>
</body>
</html>
```